Legal Information Website

We need a website that will serve as a source of information for people visiting, living, and working in the United Arab Emirates, where they can go and read about legal issues, laws, crimes, and most important find legal advice and find lawyers. The following are the pages of the website:

Find a Lawyer (Home Page)
This main feature of this page should be "Find a Lawyer"
Find a Lawyer should include the searching option by practice, by lawyer’s name, by law firm name or by location.

Ask a lawyer
This function allows the user to ask a lawyer a legal question and get an answer directly from a lawyer.

Research a legal matter
This function allows the user to do research on a certain legal topic. He/she can select from different legal topics.

Contact Us:
This page should include our contact details for the visitors in case they need any assistance. Contact us by Phone, Email, or Chat.

Once the design is approved, we will provide the rest of the website text.

Target Market(s)

General Public who seek legal advice

Industry/Entity Type

Law Firm

Font styles to use
Serif
Sans Serif

Requirements
Must have
• A tool to search for lawyer's, and then display the lawyer's picture and profile and credentials.

```html
<!DOCTYPE html>
<html lang="en">
<head>
<meta charset="utf-8">
<title>LexHarbor – Find a Lawyer</title>
<link href="https://fonts.googleapis.com/css2?family=Libre+Baskerville&family=Open+Sans:wght@400;600;700&display=swap" rel="stylesheet">
<style>
:root{
  --blue:#1a7fd0;
  --blue-dark:#0f62ad;
  --blue-light:#3aa3e4;
  --ink:#333;
  --muted:#8a8a8a;
  --dark:#2b2b2b;
  --line:#e3e3e3;
  --serif:"Libre Baskerville",Georgia,serif;
  --sans:"Open Sans",Arial,sans-serif;
}
*{margin:0;padding:0;box-sizing:border-box}
html,body{width:939px;height:1200px;overflow:hidden;background:#fff}
body{position:relative;font-family:var(--sans);color:var(--ink)}
.abs{position:absolute}

.header{top:0;left:0;width:939px;height:55px;background:#fff}
.brand{left:71px;top:12px;display:flex;align-items:center;gap:8px;font-family:var(--serif);font-size:20px;color:#2a3a4a}
.brand .dot{width:14px;height:14px;background:var(--blue-dark);border-radius:2px}
.help{left:486px;top:17px;display:flex;align-items:center;gap:8px;font-size:14px;color:#666}
.help b{font-weight:400;color:var(--blue-dark)}
.help .ico{width:16px;height:16px;background:var(--blue);border-radius:3px}
.live{left:745px;top:4px;width:136px;height:40px;border:1px solid #e5e5e5;box-shadow:0 1px 3px rgba(0,0,0,.12);padding:5px 0 0 14px}
.live .t{font-family:var(--serif);font-size:12px;color:#333;white-space:nowrap}
.live .s{font-size:9.5px;color:var(--blue)}
.live .ph{position:absolute;right:4px;top:4px;width:30px;height:30px;border-radius:50%;background:linear-gradient(#d9c2b0,#9aa9bd)}

.nav{top:55px;left:0;width:939px;height:39px;background:linear-gradient(#2a8fdc,#1466b3)}
.nav a{position:absolute;top:11px;color:#fff;text-decoration:none;font-family:var(--serif);font-size:12px;font-variant:small-caps;letter-spacing:.3px}

.hero{top:94px;left:0;width:939px;height:265px;background:linear-gradient(90deg,#f1f2f3 0%,#e4e6e9 45%,#8b94a3 70%,#6f7b8d 100%)}
.hero-photo{top:94px;left:540px;width:399px;height:265px;background:linear-gradient(90deg,rgba(240,240,240,0),#4b5d7a 40%,#3c4c66 65%,#8a939f)}
.hero-title{left:68px;top:144px;font-family:var(--serif);font-weight:400;font-size:45px;line-height:1.2;color:#333;white-space:nowrap}
.hero-sub{left:72px;top:213px;font-size:19px;line-height:29px;color:#444}

.tabs{top:359px;left:0;width:939px;height:68px;background:var(--blue-light)}
.tab{top:359px;height:68px;padding:13px 0 0 24px;border-right:1px solid rgba(0,0,0,.12)}
.tab h3{font-family:var(--serif);font-weight:400;font-size:15px;color:#fff}
.tab p{font-size:12px;color:#dfefff;margin-top:6px}
.tab p::after{content:"";display:inline-block;margin-left:5px;border:4px solid transparent;border-top:5px solid #fff;vertical-align:-2px}
.tab.active{background:linear-gradient(#2a90db,#1570c2)}
.tab.active p{color:#bcd9f3}
.pointer{left:91px;top:427px;border:9px solid transparent;border-top:9px solid #1570c2}

.search{top:427px;left:0;width:939px;height:51px;background:var(--dark)}
.field{top:441px;height:25px;background:#fff;font-size:9.5px;color:#999;padding:7px 10px}
.btn-search{left:754px;top:441px;width:117px;height:25px;background:var(--blue);border:1px solid #3d9be6;color:#fff;font-size:9.5px;font-weight:700;display:flex;align-items:center;justify-content:center;gap:6px}

.card{top:511px;width:180px;height:224px;border:1px solid var(--line);background:#fff}
.card .ph{height:129px}
.card h4{margin:15px 0 0 12px;font-size:11px;font-weight:700;color:var(--blue-dark)}
.card p{margin:6px 12px 0;font-size:9px;line-height:15px;color:var(--muted)}
.team-intro{left:685px;top:513px;width:180px}
.team-intro h2{font-family:var(--serif);font-weight:400;font-size:16px;color:#333}
.team-intro p{margin-top:12px;font-size:8.5px;line-height:13.5px;color:var(--muted)}
.btn{display:inline-block;background:var(--blue);color:#fff;font-size:9px;padding:6px 14px;margin-top:17px}
.arrows{left:690px;top:658px;display:flex;gap:6px}
.arrows span{width:19px;height:19px;border-radius:50%;border:1px solid var(--blue);display:flex;align-items:center;justify-content:center}
.arrows span.on{background:var(--blue-dark)}

.topics-title{left:82px;top:758px;font-family:var(--serif);font-weight:400;font-size:16px;color:#333}
.topics-rule{left:187px;top:769px;width:684px;border-top:3px double var(--line)}
.topic{top:798px;width:380px}
.topic .thumb{position:absolute;left:0;top:0;width:61px;height:60px}
.topic h3{margin-left:74px;font-weight:400;font-size:17px;color:#333}
.topic .meta{margin:6px 0 0 74px;display:flex;gap:14px;font-size:8.5px;color:var(--blue)}
.topic .meta span{display:flex;align-items:center;gap:4px}
.topic p{margin:14px 0 0 74px;font-size:7.5px;line-height:13.5px;color:#777}

.features{top:925px;left:0;width:939px;height:214px;background:linear-gradient(120deg,#2f74c2 0%,#1d5fab 55%,#2c79c8 100%)}
.fcard{top:968px;width:253px;height:133px;background:#fff;padding:33px 16px 0 90px}
.fcard .pic{position:absolute;left:24px;top:35px;width:49px;height:46px}
.fcard h3{font-family:var(--serif);font-weight:400;font-size:16px;color:var(--blue)}
.fcard p{margin-top:6px;font-size:7.5px;line-height:13.5px;color:#888}
.fcard a{display:block;margin-top:9px;font-size:7.5px;color:var(--blue);text-decoration:none}
.badge{top:951px;width:32px;height:31px;background:var(--blue);display:flex;align-items:center;justify-content:center}

.footer{top:1139px;left:0;width:939px;height:61px;background:#2e2e2e}
.footer .brand{left:66px;top:20px;color:#666;font-size:19px}
.footer .brand .dot{background:#555}
.finfo{top:1165px;font-size:8.5px;color:#ccc;display:flex;align-items:center;gap:6px}
.social{top:1161px;width:17px;height:17px;border-radius:50%;background:#555}
</style>
</head>
<body>

<header class="abs header">
  <div class="abs brand"><span class="dot"></span>LexHarbor</div>
  <div class="abs help"><span class="ico"></span>Get Help Now: <b>+971 02 555 0184</b></div>
  <div class="abs live"><div class="t">Live Support</div><div class="s">● Online Now</div><div class="ph" role="img" aria-label="Support agent portrait"></div></div>
</header>

<nav class="abs nav">
  <a style="left:69px">Home</a>
  <a style="left:158px">Find a Lawyer</a>
  <a style="left:296px">Ask a Lawyer</a>
  <a style="left:429px">Research a Legal Matter</a>
  <a style="left:634px">Contact Us</a>
</nav>

<section class="abs hero" role="img" aria-label="City street scene background"></section>
<div class="abs hero-photo" role="img" aria-label="Businessman in glasses talking on a phone"></div>
<h1 class="abs hero-title">Find a Lawyer.</h1>
<p class="abs hero-sub">Your #1 source for finding the best<br>lawyers in the city.</p>

<div class="abs tabs"></div>
<div class="abs tab active" style="left:68px;width:254px"><h3>Have An Urgent Problem?</h3><p>Find a Lawyer now</p></div>
<div class="abs tab" style="left:322px;width:295px;padding-left:43px"><h3>Looking for information?</h3><p>Research Legal Advice</p></div>
<div class="abs tab" style="left:617px;width:255px;padding-left:46px"><h3>Didn’t find an answer?</h3><p>Ask a Lawyer for FREE</p></div>
<div class="abs pointer"></div>

<div class="abs search"></div>
<div class="abs field" style="left:135px;width:184px">Lawyer’s First Name</div>
<div class="abs field" style="left:340px;width:184px">Lawfirm Name</div>
<div class="abs field" style="left:549px;width:184px">By Location</div>
<div class="abs btn-search"><svg width="9" height="9" viewBox="0 0 10 10"><circle cx="4" cy="4" r="3" fill="none" stroke="#fff" stroke-width="1.6"/><path d="M6.3 6.3L9 9" stroke="#fff" stroke-width="1.8"/></svg>SEARCH NOW</div>

<article class="abs card" style="left:84px"><div class="ph" role="img" aria-label="Portrait of lawyer Claire Holden" style="background:linear-gradient(#eceef1,#b9bec6)"></div><h4>Claire Holden</h4><p>Lorem ipsum dolor sit amet, teft consecte tur adipiscing elit ut eunt nisl quis augue.</p></article>
<article class="abs card" style="left:285px"><div class="ph" role="img" aria-label="Portrait of lawyer Mark Ellison" style="background:linear-gradient(#e6e8ec,#3a4150)"></div><h4>Mark Ellison</h4><p>Lorem ipsum dolor sit amet, teft consecte tur adipiscing elit ut eunt nisl quis augue.</p></article>
<article class="abs card" style="left:486px"><div class="ph" role="img" aria-label="Portrait of lawyer Dana Whitfield" style="background:linear-gradient(#eef0f2,#2d2f35)"></div><h4>Dana Whitfield</h4><p>Lorem ipsum dolor sit amet, teft consecte tur adipiscing elit ut eunt nisl quis augue.</p></article>

<div class="abs team-intro">
  <h2>Our Lawyers</h2>
  <p>Lorem ipsum dolor sit amet, consectetur adipiscing elit. Ut volutpat rutrum eros sit amet sollicitudin. Suspendisse pulvinar, velit nec pharetra niba tefra.</p>
  <span class="btn">Find More</span>
</div>
<div class="abs arrows">
  <span class="on"><svg width="7" height="8" viewBox="0 0 7 8"><path d="M5 1L2 4l3 3" fill="none" stroke="#fff" stroke-width="1.5"/></svg></span>
  <span><svg width="7" height="8" viewBox="0 0 7 8"><path d="M2 1l3 3-3 3" fill="none" stroke="#1a7fd0" stroke-width="1.5"/></svg></span>
</div>

<h2 class="abs topics-title">Legal Topics</h2>
<div class="abs topics-rule"></div>

<article class="abs topic" style="left:84px">
  <div class="thumb" role="img" aria-label="Business people meeting" style="background:linear-gradient(#d5d8dc,#4a4d55)"></div>
  <h3>Etiam tristique sagittis pulvinar</h3>
  <div class="meta"><span><svg width="10" height="10"><rect x="1" y="2" width="8" height="7" fill="none" stroke="#1a7fd0" stroke-width="1.3"/></svg>27 DEC 2013</span><span><svg width="12" height="10"><ellipse cx="6" cy="5" rx="5" ry="3.6" fill="#1a7fd0"/></svg>3</span></div>
  <p>Integer iaculis egestas odio, vel dictum turpis placerat id ellentesque semper nisl eget odio eleifend, nec blandit libero porta aliquam vel vehicula dui nam sit amet ultricies sapien.</p>
</article>
<article class="abs topic" style="left:486px">
  <div class="thumb" role="img" aria-label="Hands signing a document" style="background:linear-gradient(#f2f3f5,#b8c0cb)"></div>
  <h3>Nullam commodo felis id</h3>
  <div class="meta"><span><svg width="10" height="10"><rect x="1" y="2" width="8" height="7" fill="none" stroke="#1a7fd0" stroke-width="1.3"/></svg>25 DEC 2013</span><span><svg width="12" height="10"><ellipse cx="6" cy="5" rx="5" ry="3.6" fill="#1a7fd0"/></svg>5</span></div>
  <p>Integer iaculis egestas odio, vel dictum turpis placerat id ellentesque semper nisl veget odio eleifend, nec blandit libero porta aliquam vel vehicula dui nam sit amet ultricies sapien.</p>
</article>

<section class="abs features"></section>
<article class="abs fcard" style="left:68px"><div class="pic" role="img" aria-label="Team at work" style="background:linear-gradient(#c9d3de,#3f5a78)"></div><h3>Meet Our Team</h3><p>Lorem ipsum dolor amet, consecte tur adipiscing elit. Ut eu nisl quis augue suscipit dignissim.</p><a>Read More »</a></article>
<article class="abs fcard" style="left:344px"><div class="pic" role="img" aria-label="Support agent with headset" style="background:linear-gradient(#e4d2c4,#6b4a3a)"></div><h3>Live Support</h3><p>Lorem ipsum dolor amet, consecte tur adipiscing elit. Ut eu nisl quis augue suscipit dignissim.</p><a>Read More »</a></article>
<article class="abs fcard" style="left:620px"><div class="pic" role="img" aria-label="World map with connections" style="background:linear-gradient(#d9e6f2,#2f6aa3)"></div><h3>We Speak</h3><p>Lorem ipsum dolor amet, consecte tur adipiscing elit. Ut eu nisl quis augue suscipit dignissim.</p><a>Read More »</a></article>
<div class="abs badge" style="left:178px"><svg width="14" height="14"><circle cx="7" cy="4" r="3" fill="#fff"/><path d="M1 13c0-4 12-4 12 0z" fill="#fff"/></svg></div>
<div class="abs badge" style="left:454px"><svg width="14" height="14"><rect x="1" y="1" width="12" height="12" rx="2" fill="none" stroke="#fff" stroke-width="1.5"/><path d="M4 4c0 3 3 6 6 6" stroke="#fff" stroke-width="2" fill="none"/></svg></div>
<div class="abs badge" style="left:730px"><svg width="16" height="13"><ellipse cx="7" cy="5" rx="6" ry="4.3" fill="#fff"/><path d="M3 8l-1 4 4-3z" fill="#fff"/></svg></div>

<footer class="abs footer">
  <div class="abs brand"><span class="dot"></span>LexHarbor</div>
</footer>
<div class="abs finfo" style="left:348px"><svg width="10" height="8"><rect width="10" height="8" fill="#999"/></svg>contact@lexharbor.com</div>
<div class="abs finfo" style="left:487px"><svg width="9" height="9"><path d="M1 1h3l1 2-1.5 1a5 5 0 002.5 2.5L7 5l2 1v3C4 9 1 5 1 1z" fill="#999"/></svg>(Toll FREE) +123 555 0199</div>
<div class="abs finfo" style="left:624px">Copyright 2014. LexHarbor | All Rights Reserved</div>
<div class="abs social" style="left:827px"></div>
<div class="abs social" style="left:853px"></div>

</body>
</html>
```